TRV Mechanical Solutions Business Card Design

Business card design

Thinking just large logo on one side with a phone number and the back side is contact info with services we offer with a industrial plant across the bottom of the card

See must haves. I will be laser etching these business cards on black metal business cards as well as full color card stock. So must be bold and professional.

Target Market(s)

Industrial manufacturing

Contact Information for Business Card

Industrial manufacturing construction business specializing in consulting project managment and completing projects turn key

Font styles to use
Other font styles liked:
• See Logo for colors and font style

Requirements
Must have
• TRV Mechanical Solutions
• Gerald Munroe
• 2847 Alderwick Lane
• Bel Air, MD, 21047
• Project Managment
• Consulting
• Turn Key Industrial Projects
• I’d like a industrial manufacturing “cityline” on the back side bottom of the
• I’d like to be able to print these business cards in regular color on card stock but I’d also like the design to be etched into black metal business cards

```html
<!DOCTYPE html>
<html lang="en">
<head>
<meta charset="UTF-8">
<title>TRV Mechanical Solutions – Business Card</title>
<link rel="stylesheet" href="https://fonts.googleapis.com/css2?family=Source+Sans+3:wght@600&display=swap">
<style>
  :root {
    --backdrop: #d8d8d8;
    --frame: #9a9a9a;
    --card: #ffffff;
    --shadow: rgba(0, 0, 0, 0.45);
    --ink: #111111;
    --logo-grey: #7b7b7b;
    --brand-blue: #0b9fe0;
    --skyline-light: #2cc3f2;
    --skyline-dark: #0a8ad3;
  }
  * { margin: 0; padding: 0; box-sizing: border-box; }
  html, body {
    width: 1200px;
    height: 1196px;
    overflow: hidden;
    background: var(--backdrop);
  }
  .sheet {
    position: relative;
    width: 1200px;
    height: 1196px;
    border: 2px solid var(--frame);
    background: var(--backdrop);
    font-family: "Source Sans 3", "Myriad Pro", Arial, sans-serif;
    font-weight: 600;
  }
  .card {
    position: absolute;
    left: 41px;
    width: 1118px;
    height: 545px;
    background: var(--card);
    box-shadow: 5px 6px 6px var(--shadow);
    overflow: hidden;
  }
  .card--front { top: 31px; }
  .card--back  { top: 593px; }

  .brand {
    position: absolute;
    left: 0;
    right: 0;
    top: 238px;
    display: flex;
    justify-content: center;
    align-items: center;
    gap: 22px;
  }
  .brand__square {
    width: 58px;
    height: 58px;
    background: var(--brand-blue);
  }
  .brand__name {
    font-size: 58px;
    line-height: 1;
    color: var(--logo-grey);
    letter-spacing: 0.2px;
  }

  .contact {
    position: absolute;
    left: 108px;
    top: 132px;
    color: var(--ink);
    line-height: 1.2;
  }
  .contact__company { font-size: 37px; }
  .contact__company-mark { font-size: 41px; }
  .contact__name { font-size: 34px; margin-top: 6px; }
  .contact__address { font-size: 29px; margin-top: 6px; line-height: 1.42; }
  .contact__services { font-size: 23px; margin-top: 4px; line-height: 1.48; list-style: none; }

  .skyline {
    position: absolute;
    left: 653px;
    top: 170px;
    width: 465px;
    height: 375px;
    background: linear-gradient(90deg, var(--skyline-light), var(--skyline-dark));
    -webkit-mask-image: linear-gradient(180deg, transparent 0%, rgba(0,0,0,0.35) 25%, #000 60%);
    mask-image: linear-gradient(180deg, transparent 0%, rgba(0,0,0,0.35) 25%, #000 60%);
  }
</style>
</head>
<body>
  <div class="sheet">
    <section class="card card--front">
      <div class="brand">
        <span class="brand__square"></span>
        <span class="brand__name">TRV Mechanical Solutions</span>
      </div>
    </section>

    <section class="card card--back">
      <div class="contact">
        <p class="contact__company"><span class="contact__company-mark">TRV</span> Mechanical Solutions</p>
        <p class="contact__name">Gerald Munroe</p>
        <p class="contact__address">2847 Alderwick Lane<br>Bel Air , MD, 21047</p>
        <ul class="contact__services">
          <li>Project Manangement</li>
          <li>Consulting</li>
          <li>Turn Key Industrial Projects</li>
        </ul>
      </div>
      <div class="skyline" role="img" aria-label="Blue industrial plant cityline silhouette of factory buildings and stacks along the bottom right of the card"></div>
    </section>
  </div>
</body>
</html>
```